New wine label design aimed at millennials

We have developed 2 new quality wines - a crisp, cool climate Chardonnay from the Orange region and a spicy Shiraz from the Gundagai wine region.

Each of these wines have been made in a distinctly modern style, with less oak and more elegance than most and come from two relatively new but exciting wine regions.

They are distinctly food friendly as a result.

These are classic varieties, with a modern take from 'undiscovered' regions.

We are seeking to target millennial wine drinkers who are possibly new to wine or are early in their journey into wine.

We are after a contemporary single label design (i.e. - not a font ab back label) to be applied to a 'lean green' burgundy bottle that speaks to the modern take on classic varieties from undiscovered regions.

We have already recieved a umber of good designs based on some possible brand names:

Meridell
Kettle and Compass
The Copper Lamplightar

And now we would like to purse labels focusing just on Kettle and Compass (of course if a bolt of lightening strikes you on the other names, feel free!)

the reference to Kettle and Compass comes from a story attached to one of our existing labels – Beatrice Thornbury. The two Thornbury brothers who founded this Vineyard famously borrowed a Kettle and Compass from a well-established winery family in order for them to roam the local foothills in order to find their ideal vineyard site.

We would like to capture this sense of exploration and discovery in what would form a sub-tier label for this brand.

It would still be targeting very much millennial's and so we want the label to look contemporary and urban, but reflect the sense of exploration and discovery awhile referencing the historical authenticity of the whole overarching brand structure.

I have attached a number of inspirational images that would need to be translated into a more modern visual setting.

obviously use of a horse and a matter in some sort of "branded" image would be a first step and obviously the historical/authentic back story combined with a modern anaesthetic lends itself to plain black-and-white.

However, clever use of a modern colour palette would also be very welcome.
Updates

For further inspiration we have been considering the following phrases and words as possible label namesGallivant - giving a sense of freewheeling adventure and explorationHorse & Mattock - referencing an old story of 2 pioneer vignerons being lent a horse and a mattock to go out and find their ideal vineyard sites, introducing concepts of innovation, discovery and authenticityThe Gentleman Vigneron - referencing a founding winemakers nominal descriptor of himself and bringing a true element of authenticity and quality. Added Monday, July 31, 2017

Project Deadline Extended Reason: I am hoping to give some more information and focus on the desired outcomes.The name of the label will be Kettle and Compass.Please review the prior comments to get the background on this and I will add more information as well.I will try to identify and provide some other design work that aligns with what we are trying to achieve also. Added Friday, August 11, 2017

Target Market(s)

Millennials, skewing female 21-35 years, university educated, employed in white collar or professional industry, urban

Font styles to use
Serif
Sans Serif

Colors

Designer to choose colors to be used in the design.

Requirements
Must have
• Modern, contemporary urban look and feel that stands out on the shelf.
• Must be relevant and attractive to millennials.
• Sense of humour or quirkiness to it.
• We like this label amongst many other
• http://www.pelmarkcellars.com/shopwines/
Nice to have
• We will aim to use recycled/low carbon footprint glass in the packaging (i.e. the lean green bottles) so would also aim to use 100% recycled paper on the label and would like to mention this in the design.

```html
<!DOCTYPE html>
<html lang="en">
<head>
<meta charset="utf-8">
<title>Kettle &amp; Compass — Cabernet Sauvignon 2017</title>
<link href="https://fonts.googleapis.com/css2?family=Gochi+Hand&family=Federo&display=swap" rel="stylesheet">
<style>
  :root {
    --page: #ffffff;
    --lime: #d8f21a;
    --lime-deep: #c4e010;
    --ink: #111111;
    --magenta: #ff19e6;
    --magenta-deep: #c20fb0;
  }
  html, body {
    margin: 0;
    padding: 0;
    width: 1122px;
    height: 1200px;
    overflow: hidden;
    background: var(--page);
  }
  .canvas {
    position: relative;
    width: 1122px;
    height: 1200px;
  }
  .label {
    position: absolute;
    left: 121px;
    top: 118px;
    width: 880px;
    height: 880px;
    background: radial-gradient(circle at 50% 45%, var(--lime) 0%, var(--lime) 55%, var(--lime-deep) 100%);
    overflow: hidden;
  }
  .label-frame {
    position: absolute;
    inset: 0;
  }
  .corner-ornament {
    position: absolute;
    width: 80px;
    height: 80px;
    background: rgba(17, 17, 17, 0.18);
    border-radius: 4px;
  }
  .corner-ornament.top-left { left: 22px; top: 22px; }
  .corner-ornament.top-right { right: 22px; top: 22px; }
  .corner-ornament.bottom-left { left: 22px; bottom: 22px; }
  .corner-ornament.bottom-right { right: 22px; bottom: 22px; }

  .emblem-art {
    position: absolute;
    left: 60px;
    top: 240px;
    width: 760px;
    height: 170px;
    border-radius: 90px;
    background: linear-gradient(100deg, var(--magenta) 0%, var(--magenta-deep) 30%, #3a1436 60%, var(--ink) 100%);
    opacity: 0.85;
  }
  .brand-first {
    position: absolute;
    left: 116px;
    top: 90px;
    margin: 0;
    font-family: "Gochi Hand", cursive;
    font-weight: 400;
    font-size: 130px;
    line-height: 1;
    letter-spacing: 2px;
    color: var(--ink);
    transform: scaleY(1.5);
    transform-origin: top left;
    white-space: nowrap;
  }
  .brand-second {
    position: absolute;
    left: 298px;
    top: 392px;
    margin: 0;
    display: flex;
    align-items: baseline;
    font-family: "Gochi Hand", cursive;
    font-weight: 400;
    color: var(--ink);
    line-height: 1;
    white-space: nowrap;
  }
  .brand-second .ampersand {
    font-size: 200px;
    margin-right: 10px;
  }
  .brand-second .word {
    font-size: 90px;
    letter-spacing: 2px;
  }
  .variety-ribbon {
    position: absolute;
    left: 140px;
    top: 618px;
    width: 600px;
    height: 90px;
  }
  .variety-name {
    position: absolute;
    left: 140px;
    top: 618px;
    width: 600px;
    height: 78px;
    margin: 0;
    display: flex;
    align-items: center;
    justify-content: center;
    font-family: "Federo", sans-serif;
    font-size: 50px;
    color: var(--ink);
  }
  .vintage {
    position: absolute;
    left: 0;
    right: 0;
    top: 728px;
    margin: 0;
    text-align: center;
    font-family: "Federo", sans-serif;
    font-size: 44px;
    letter-spacing: 2px;
    color: var(--ink);
  }
</style>
</head>
<body>
<main class="canvas">
  <section class="label">
    <svg class="label-frame" width="880" height="880" viewBox="0 0 880 880" aria-hidden="true">
      <line x1="115" y1="40" x2="765" y2="40" stroke="#111" stroke-width="3"/>
      <line x1="115" y1="52" x2="765" y2="52" stroke="#111" stroke-width="1.5"/>
      <line x1="115" y1="828" x2="765" y2="828" stroke="#111" stroke-width="1.5"/>
      <line x1="115" y1="840" x2="765" y2="840" stroke="#111" stroke-width="3"/>
      <line x1="40" y1="115" x2="40" y2="765" stroke="#111" stroke-width="2"/>
      <line x1="840" y1="115" x2="840" y2="765" stroke="#111" stroke-width="2"/>
    </svg>
    <div class="corner-ornament top-left" role="img" aria-label="Scrolled corner flourish"></div>
    <div class="corner-ornament top-right" role="img" aria-label="Scrolled corner flourish"></div>
    <div class="corner-ornament bottom-left" role="img" aria-label="Scrolled corner flourish"></div>
    <div class="corner-ornament bottom-right" role="img" aria-label="Scrolled corner flourish"></div>

    <div class="emblem-art" role="img" aria-label="Distressed black and magenta illustration of a leaping horse beside a pick tool"></div>

    <h1 class="brand-first">KETTLE</h1>
    <p class="brand-second"><span class="ampersand">&amp;</span><span class="word">COMPASS</span></p>

    <svg class="variety-ribbon" width="600" height="90" viewBox="0 0 600 90" aria-hidden="true">
      <polygon points="0,14 60,14 60,90 0,90 20,52" fill="#c20fb0" stroke="#111" stroke-width="3"/>
      <polygon points="600,14 540,14 540,90 600,90 580,52" fill="#c20fb0" stroke="#111" stroke-width="3"/>
      <rect x="40" y="0" width="520" height="78" fill="#ff19e6" stroke="#111" stroke-width="3"/>
    </svg>
    <p class="variety-name">Cabernet Sauvignon</p>
    <p class="vintage">2017</p>
  </section>
</main>
</body>
</html>
```